Looking to overhaul my current Wordpress website

Current have a website www.qoradatrix.com in wordpress, lack the skills or design flare to make it look and work better and more corporate professional.
We are a technology solution provider and software developer.
Updates
I think i have successfully uploaded my logo to assist with the wordpress theme and framework samples you will be providing.
Post me a message if you can locate it.
Target Market(s)
Small to business
Industry/Entity Type
Software
Font styles to use
Sans Serif
Requirements
Must have
- Must work on any device anywhere anytime, mobile ready in addition to traditional browser. Must be in work press for ongoing maintenance.
Nice to have
- use these website for a look and feel http://www.fernwaleclear.com.au/ http://www.tarvolinadvisory.com/work http://www.tarvolinadvisory.com/method
http://www.plumcrestlab.com/
Should not have
- No Flash!!,

```html
<!DOCTYPE html>
<html lang="en">
<head>
<meta charset="utf-8">
<title>Qoradatrix — Software Engineering &amp; Development</title>
<link rel="stylesheet" href="https://fonts.googleapis.com/css2?family=Carlito:wght@400;700&family=Questrial&family=Poppins:wght@500;600&family=Abel&display=swap">
<style>
:root{
  --header-bg:#f3f3f3;
  --hero-blue:#06aef0;
  --band-dark:#1f1f1f;
  --heading-blue:#0e68b0;
  --link-blue:#1b9bd8;
  --button-blue:#1a7fd8;
  --text:#333333;
  --muted:#555555;
  --card-border:#dddddd;
  --soft-grey:#ededed;
  --footer-bg:#242424;
  --white:#ffffff;
}
*{margin:0;padding:0;box-sizing:border-box}
html,body{width:1200px;height:2417px;overflow:hidden}
body{position:relative;background:var(--white);color:var(--text);font-family:"Carlito",Arial,sans-serif}
.abs{position:absolute}

/* header */
.site-header{left:0;top:0;width:1200px;height:132px;background:var(--header-bg);border-bottom:1px solid #e2e2e2}
.brand{left:74px;top:38px;font-family:"Carlito",sans-serif;font-size:40px;color:#222;letter-spacing:.5px}
.main-nav{right:70px;top:47px;display:flex;align-items:center;gap:22px;font-family:"Carlito",sans-serif;font-size:17px;color:#222}
.nav-cta{background:var(--button-blue);color:var(--white);padding:6px 12px;border-radius:4px}

/* hero */
.hero{left:0;top:132px;width:1200px;height:455px;background:var(--hero-blue)}
.hero-device{left:93px;top:52px;width:416px;height:344px;border-radius:22px;background:linear-gradient(160deg,#3a3a3a,#111);}
.hero-device .screen{position:absolute;left:38px;top:30px;width:340px;height:284px;background:linear-gradient(180deg,#f7f7f7,#dfe6ec);border-radius:2px}
.hero-title{right:90px;top:120px;text-align:right;font-family:"Questrial",sans-serif;color:var(--white);font-size:44px;line-height:46px;letter-spacing:.5px}
.hero-title .amp{position:absolute;right:-52px;top:18px;font-family:"Poppins",sans-serif;font-weight:600;font-size:62px}
.hero-text{left:553px;top:218px;width:550px;text-align:right;font-family:"Questrial",sans-serif;color:var(--white);font-size:19px;line-height:26px}
.hero-btn{left:847px;top:313px;width:248px;height:56px;border:2px solid var(--white);border-radius:4px;display:flex;align-items:center;justify-content:center;gap:12px;color:var(--white);font-family:"Questrial",sans-serif;font-size:21px}

.tagline{left:0;top:587px;width:1200px;height:75px;background:var(--band-dark);color:var(--white);font-family:"Abel",sans-serif;font-size:25px;display:flex;align-items:center;justify-content:center;letter-spacing:.3px}

/* section headings */
.section-title{left:0;width:1200px;text-align:center;font-family:"Poppins",sans-serif;font-weight:600;color:var(--heading-blue);font-size:38px;letter-spacing:.5px}
.section-sub{left:0;width:1200px;text-align:center;font-family:"Questrial",sans-serif;color:var(--text);font-size:19px}

/* expertise cards */
.card{top:802px;width:251px;height:286px;border:2px solid var(--card-border);background:var(--white)}
.card .thumb{position:absolute;left:8px;top:8px;width:231px;height:198px}
.card .label{position:absolute;left:0;top:226px;width:100%;text-align:center;font-family:"Questrial",sans-serif;color:var(--link-blue);font-size:19px;line-height:20px}

/* values */
.value{top:1264px;width:330px}
.value-head{display:flex;align-items:center;gap:14px;font-family:"Carlito",sans-serif;font-weight:700;font-size:20px;color:#333;height:44px}
.value-lead{margin-top:38px;font-weight:700;font-size:16px;line-height:22px;color:#222}
.value-body{font-size:16px;line-height:22px;color:var(--muted)}

/* welcome */
.welcome-title{font-size:42px;letter-spacing:0}
.welcome-copy{left:82px;top:1586px;width:1040px;font-size:15.5px;line-height:21px;color:#333}
.welcome-copy p{margin-bottom:20px}
.welcome-copy p.tight{margin-bottom:0}
.btn-blue{left:78px;top:1789px;width:124px;height:41px;background:var(--button-blue);border-radius:8px;color:var(--white);font-family:"Questrial",sans-serif;font-size:19px;display:flex;align-items:center;justify-content:center}

/* get started */
.started{left:0;top:1893px;width:1200px;height:354px;background:var(--soft-grey)}
.quote-btn{left:447px;top:2074px;width:316px;height:78px;background:var(--band-dark);border-radius:8px;color:var(--white);font-family:"Questrial",sans-serif;font-size:32px;display:flex;align-items:center;justify-content:center}

/* footer */
.site-footer{left:0;top:2247px;width:1200px;height:170px;background:var(--footer-bg)}
.footer-col{top:2270px;width:240px;color:var(--white);font-size:15px;line-height:25px}
.footer-col h3{font-family:"Carlito",sans-serif;font-weight:400;font-size:21px;margin-bottom:12px}
.social{display:flex;gap:6px;margin-top:6px}
.social span{width:30px;height:30px;border-radius:50%;display:block}
</style>
</head>
<body>

<header class="abs site-header">
  <div class="abs brand">Qoradatrix</div>
  <nav class="abs main-nav">
    <span>Home</span><span>Our team</span><span>Our Values</span><span>Working with us</span><span>Our Services</span><span>Our Solutions</span><span class="nav-cta">Get in Touch</span>
  </nav>
</header>

<section class="abs hero">
  <div class="abs hero-device" role="img" aria-label="Tablet showing a sports web application on screen"><div class="screen"></div></div>
  <h1 class="abs hero-title">SOFTWARE ENGINEERING<br>DEVELOPMENT<span class="amp">&amp;</span></h1>
  <p class="abs hero-text">In a company like Qoradatrix, engineering and creativity drives the business. Our people are all a aligned to creating well architected, extensible, highly scalable applications.</p>
  <div class="abs hero-btn">Learn More
    <svg width="22" height="22" viewBox="0 0 22 22"><circle cx="11" cy="11" r="9.5" fill="none" stroke="#fff" stroke-width="2"/><path d="M8 6.5l5 4.5-5 4.5M7 11h6" fill="none" stroke="#fff" stroke-width="2"/></svg>
  </div>
</section>

<div class="abs tagline">We are a diverse group of experienced designers, strategists and technologists ready to make things happen</div>

<h2 class="abs section-title" style="top:684px">OUR EXPERTISE</h2>
<p class="abs section-sub" style="top:752px">Pushing the limits in creating a digital minded future in web and software world</p>

<div class="abs card" style="left:83px"><div class="thumb" role="img" aria-label="Server racks in a dark data centre" style="background:linear-gradient(180deg,#2a2a2e,#6b1d22 60%,#1a1a1c)"></div><div class="label">Technology Strategy</div></div>
<div class="abs card" style="left:344px"><div class="thumb" role="img" aria-label="Close-up of a laptop keyboard" style="background:linear-gradient(160deg,#e9eef2,#9aa5ae)"></div><div class="label">Wireless Infrastructure<br>Services</div></div>
<div class="abs card" style="left:602px"><div class="thumb" role="img" aria-label="Hand sketching a flow chart on glass" style="background:linear-gradient(160deg,#f4f4f4,#c9c4c2)"></div><div class="label">Mobile Forms</div></div>
<div class="abs card" style="left:860px"><div class="thumb" role="img" aria-label="Business team working at a laptop" style="background:linear-gradient(160deg,#dfe4ea,#3a4a63)"></div><div class="label">Consulting &amp; Advisory</div></div>

<h2 class="abs section-title" style="top:1132px">OUR VALUES</h2>
<p class="abs section-sub" style="top:1201px">We assist you with your thinkng and our expertise</p>

<div class="abs value" style="left:80px">
  <div class="value-head"><svg width="34" height="40" viewBox="0 0 34 40"><circle cx="17" cy="15" r="12" fill="none" stroke="#1b9bd8" stroke-width="2.5"/><path d="M12 29h10M13 34h8" stroke="#1b9bd8" stroke-width="2.5"/></svg>Beautiful Products</div>
  <p class="value-lead">We love to build beautiful applications<br>and solutions.</p>
  <p class="value-body">Beautiful products look great and work in a simple, intuitive manner and the user wants to use the product all the time.....</p>
</div>
<div class="abs value" style="left:452px">
  <div class="value-head"><svg width="40" height="40" viewBox="0 0 40 40"><circle cx="20" cy="20" r="17" fill="none" stroke="#1b9bd8" stroke-width="2.5"/><ellipse cx="20" cy="20" rx="7" ry="17" fill="none" stroke="#1b9bd8" stroke-width="2"/><path d="M3 20h34M6 11h28M6 29h28" stroke="#1b9bd8" stroke-width="2"/></svg>Working with Good People</div>
  <p class="value-lead">“Red Pill”, “Blue Pill” there is no quick<br>fix.</p>
  <p class="value-body">There is no process, toolkit, or magic potion that guarantees that a team will create complex software....</p>
</div>
<div class="abs value" style="left:829px">
  <div class="value-head"><svg width="38" height="40" viewBox="0 0 38 40"><circle cx="19" cy="12" r="8" fill="none" stroke="#1b9bd8" stroke-width="2.5"/><path d="M4 38c0-10 7-16 15-16s15 6 15 16z" fill="none" stroke="#1b9bd8" stroke-width="2.5"/></svg>No Fluff &amp; Fru Fru</div>
  <p class="value-lead">We focus on results, not planning<br>documents and artifacts.</p>
  <p class="value-body">It’s never possible to plan everything up-front.Which is why we choose to employ......</p>
</div>

<h2 class="abs section-title welcome-title" style="top:1505px">Welcome To Qoradatrix</h2>
<div class="abs welcome-copy">
  <p>Qoradatrix was founded in 2007 with the mission to become the go-to technology consultancy for building world-class, one of a kind, web applications and web based businesses.</p>
  <p class="tight">We have seen many great ideas killed because of poor execution by technology teams that didn’t treat their work as craft.</p>
  <p>We knew we could provide the perfect place for entrepreneurs to come for founder level design and engineering leadership, and where large companies could inject entrepreneurial innovation into their existing product development efforts.</p>
  <p>Our team of engineers, product management, user experience and design talent is our dream-team of talent we will use on our own products, such as Vellum Notes CRM, and also the same team our clients have access to.</p>
</div>
<div class="abs btn-blue">Read More</div>

<section class="abs started"></section>
<h2 class="abs section-title" style="top:1940px">LET’S GET STARTED</h2>
<p class="abs section-sub" style="top:2008px">Learn how we can turn your ideas in to reality</p>
<div class="abs quote-btn">Request A Quote</div>

<footer class="abs site-footer"></footer>
<div class="abs footer-col" style="left:93px"><h3>Contact Us</h3>Ph: 08 5550 1274<br>sales@qoradatrix.com.au</div>
<div class="abs footer-col" style="left:371px"><h3>Our Address</h3>Qoradatrix<br>42 Brindle Lane, Harlow Court<br>Sydney, Australia</div>
<div class="abs footer-col" style="left:649px"><h3>Social Networks</h3>Join the conversation
  <div class="social"><span style="background:#3b5a98"></span><span style="background:#3a9ad9"></span><span style="background:#d34836"></span><span style="background:#1b77b5"></span></div>
</div>
<div class="abs footer-col" style="left:928px;width:200px"><h3>Legal Stuff</h3>© Copyright 2013, All rights reserved, Qoradatrix</div>

</body>
</html>
```